Professional and modern website for Real Estate services company

Hi there! We're looking for a responsive, highly professional and modern (in line with Latest trends) coded website for a Real Estate services company named Portales720º (find logo attached). I will try to Explain how I picture it in my head, but feel free to step out of the script and design it as you please. The structure for the website must be as Follows: - Menu: at the top of the screen, always visible (in any page and when to scrolling down). Logo at the left hand side (clicking redirects to home), then a Services, About us, Blog and Contact and on the right hand, Estimate and Log in (just placeholder, no log in required yet). - Home: (I like https://fr.velmora.example/): a landscape picture of Madrid's skyline. Very important That at a first glance (without scrolling) you can see a box to input data of your building to get an estimate (Post code, Number of homes, Number of garages, Number of stores, Swimming pool (yes / no) Concierge (yes / no)). Should there be a small space Also for a corporate presentation video (more or less like https://www.bravunecasales.example/ but With the estimate Request box INSTEAD OF the App - however, do not take this one as example Given I just wanted to illustrate the structure). Still in the Home, bellow the first glance, I'd like to have a brief introduction of the following pages (Services, About us, Blog and Contact). This can be in a Either "square" form (like https://fr.velmora.example/) or in a "scroll" form (like https://k7portales.example/). - Services: we offer 3 sets of services, each of them composed by three specific services, Namely: * Administration Treasury Accounting Savings * Consulting Legal Technical Regulatory * Mediation Repairs Meetings Delinquency For the sake of structuring, each of the nine services will Have to written description composed of 3 small paragraphs of About 15 words. I Tend to like to Accompany With each of the services related icons / vectors, but feel free to design them as you want. - About us: content not yet defined, but will be a series of bullets / sections in Which We talk about prep or differentiating points. We can include the corporate video presentation here again. - Blog: just a space Where you can see to the blog entries (in Home, probably just show 3/4). - Contact: a fancy contact form, with map, address, telephone, e-mail and opening hours. Just to give it a bit more content, maybe include a catch phrase like "We're looking forward to meeting you!" or something like that. - Estimate: this is the Most Important page in the website (in Addition to the upper part of the Home page). Basically replicate the estimate for the home box, but maybe with a bit more design or extended, Given this is a single page just for that. - Log in: opens a drop-down with user and password (just placeholder, no log in required yet). Regarding colors, we still do not Have a color scheme, so anything in line With the logo is OK. Many thanks in advance, Martin

Target Market(s)

All ages and genders

Industry/Entity Type

Real Estate

Coding

Coded - Design and coding required

Number of Pages Required

5+ page

Font styles to use
Sans Serif

Requirements
Must have
• Blank colored background

```html
<!DOCTYPE html>
<html lang="en">
<head>
<meta charset="utf-8">
<title>Contact Us – Portales720º</title>
<link href="https://fonts.googleapis.com/css2?family=Jost:wght@300;400;500&family=Lato:wght@400;700&display=swap" rel="stylesheet">
<style>
:root{
  --orange:#e07b14;
  --submit:#f15a22;
  --bar:#d4650a;
  --ink:#2b2b2b;
  --muted:#666;
  --line:#d6d6d6;
  --topbar:#f2f2f2;
  --footer:#5f5f5f;
  --field-dark:#6c6c6c;
  --map-a:#f3efe3;
  --map-b:#e8e2cf;
}
*{box-sizing:border-box;margin:0;padding:0}
html,body{width:890px;height:1200px;overflow:hidden;background:#fff}
body{font-family:"Lato",sans-serif;color:var(--ink);position:relative}
.abs{position:absolute}
.topbar{left:0;top:0;width:890px;height:30px;background:var(--topbar);font-size:12px;color:var(--muted)}
.topbar .item{top:8px;display:flex;align-items:center;gap:6px;white-space:nowrap}
.social{display:flex;gap:14px}
.social span{width:9px;height:9px;border-radius:50%;background:currentColor;display:block}
.header{left:0;top:30px;width:890px;height:57px;background:#fff;border-bottom:1px solid #e4e4e4}
.brand{left:75px;top:15px;font-family:"Lato",sans-serif;font-weight:700;font-size:22px;color:var(--ink);display:flex;align-items:center;gap:6px}
.brand i{width:10px;height:10px;background:var(--orange);display:block}
.nav a{position:absolute;top:22px;font-size:12px;color:var(--ink);text-decoration:none;white-space:nowrap}
.nav a.active{color:var(--orange)}
.section-title{left:0;width:890px;text-align:center;font-family:"Jost",sans-serif;font-weight:400;font-size:31px;color:#444}
.divider{left:329px;width:232px;height:12px}
.info{top:214px;display:flex;gap:8px;white-space:nowrap}
.info h3{font-size:14px;font-weight:700;margin-bottom:3px}
.info p{font-size:11px}
.map{background:linear-gradient(135deg,var(--map-a),var(--map-b));border:1px solid #cfcfcf}
.field{border:1px solid var(--line);height:41px;font-size:12px;font-weight:700;padding:14px 12px;color:#333}
.submit{left:73px;top:902px;width:67px;height:25px;background:var(--submit);color:#fff;font-family:"Jost",sans-serif;font-weight:500;font-size:14px;letter-spacing:.5px;text-align:center;line-height:25px}
.footer{left:0;top:954px;width:890px;height:218px;background:var(--footer);color:#fff}
.footer h4{position:absolute;font-family:"Jost",sans-serif;font-weight:300;font-size:16px}
.footer .rule{position:absolute;height:1px;background:#777}
.links{left:90px;top:1024px;font-size:9.5px;color:#fff;list-style:none;line-height:25px}
.links li::before{content:"›";color:#999;margin-left:-12px;margin-right:7px}
.ffield{left:223px;width:144px;height:21px;background:var(--field-dark);font-size:8.5px;padding:5px 7px;color:#ddd}
.fbtn{left:227px;top:1114px;width:59px;height:21px;background:var(--bar);font-size:10px;font-weight:700;text-align:center;line-height:21px}
.details{left:432px;font-size:9.5px;line-height:14px;white-space:nowrap}
.details b{font-weight:700}
.dot{position:absolute;left:432px;width:7px;height:7px;border-radius:50%;background:var(--orange)}
.bottombar{left:0;top:1172px;width:890px;height:28px;background:var(--bar);color:#fff;font-size:10px}
</style>
</head>
<body>

<div class="abs topbar">
  <div class="abs item" style="left:74px">
    <svg width="12" height="9" viewBox="0 0 12 9"><rect width="12" height="9" fill="var(--orange)"/><path d="M0 0l6 5 6-5" stroke="#fff" fill="none"/></svg>
    info@portales720.example
  </div>
  <div class="abs item" style="left:268px">
    <svg width="10" height="10" viewBox="0 0 10 10"><path d="M2 0l2 2-1 2 3 3 2-1 2 2-2 2C4 10 0 6 0 2z" fill="var(--orange)"/></svg>
    (012) 5550 1827
  </div>
  <div class="abs social" style="left:752px;top:11px;color:#444"><span></span><span></span><span></span></div>
</div>

<div class="abs header">
  <div class="abs brand"><span>Portales720º</span><i></i></div>
  <nav class="nav">
    <a style="left:315px">About Us</a>
    <a style="left:396px">Services</a>
    <a style="left:475px">Blog</a>
    <a class="active" style="left:532px">Contact Us</a>
    <a style="left:680px"><span style="color:var(--orange);font-weight:700;margin-right:6px">$</span>Estimate</a>
    <a style="left:770px"><span style="color:var(--orange);margin-right:6px">➜</span>Log In</a>
  </nav>
</div>

<h1 class="abs section-title" style="top:112px">Contact Us</h1>
<svg class="abs divider" style="top:157px" viewBox="0 0 232 12"><path d="M0 6h102l14-10 14 10h102" transform="translate(0 4)" stroke="#999" fill="none" stroke-width="1"/></svg>

<div class="abs info" style="left:157px">
  <svg width="20" height="30" viewBox="0 0 20 30"><path d="M4 0l5 6-3 4 6 10 4-2 4 6-5 5C8 28 0 14 0 4z" fill="var(--orange)"/></svg>
  <div><h3>Call Us Today</h3><p>123-555-0190</p></div>
</div>
<div class="abs info" style="left:323px">
  <svg width="26" height="34" viewBox="0 0 26 34"><path d="M13 0a13 13 0 0113 13c0 9-13 21-13 21S0 22 0 13A13 13 0 0113 0z" fill="var(--orange)"/><circle cx="13" cy="13" r="5" fill="#fff"/></svg>
  <div style="margin-left:10px"><h3>Portales 720</h3><p>123 enim ad minim veniaml, nostrud exerci</p></div>
</div>
<div class="abs info" style="left:614px">
  <svg width="20" height="14" viewBox="0 0 20 14"><rect width="20" height="14" fill="var(--orange)"/><path d="M0 0l10 8 10-8" stroke="#fff" fill="none"/></svg>
  <div style="margin-left:8px"><h3>Email Us</h3><p>inqiry@portales720.example</p></div>
</div>

<div class="abs map" role="img" aria-label="Road map of Kansas and Oklahoma with a red pin marking the office location" style="left:73px;top:300px;width:744px;height:319px"></div>

<h2 class="abs section-title" style="top:642px">Quick Inquiry</h2>
<svg class="abs divider" style="top:689px" viewBox="0 0 232 12"><path d="M0 6h102l14-10 14 10h102" transform="translate(0 4)" stroke="#999" fill="none" stroke-width="1"/></svg>

<div class="abs field" style="left:73px;top:729px;width:178px">Name</div>
<div class="abs field" style="left:263px;top:729px;width:178px">Email</div>
<div class="abs field" style="left:454px;top:729px;width:178px">Phone</div>
<div class="abs field" style="left:638px;top:729px;width:179px">Type of Service<span style="position:absolute;right:6px;color:var(--orange);font-size:9px">⌄</span></div>
<div class="abs field" style="left:73px;top:786px;width:744px;height:104px">Message</div>
<div class="abs submit">SUBMIT</div>

<div class="abs footer">
  <h4 style="left:77px;top:30px">Quick Links</h4>
  <div class="rule" style="left:77px;top:58px;width:90px"></div>
  <h4 style="left:223px;top:30px">Quick Inquiry</h4>
  <div class="rule" style="left:223px;top:58px;width:150px"></div>
  <h4 style="left:432px;top:30px">Contact Details</h4>
  <div class="rule" style="left:432px;top:58px;width:155px"></div>
  <div class="rule" style="left:195px;top:70px;width:1px;height:95px"></div>
  <div class="rule" style="left:403px;top:70px;width:1px;height:95px"></div>
</div>
<ul class="abs links"><li>Home</li><li>About Us</li><li>Services</li><li>Blog</li><li>Contact Us</li></ul>
<div class="abs ffield" style="top:1028px">Name</div>
<div class="abs ffield" style="top:1057px">Email</div>
<div class="abs ffield" style="top:1083px">Message</div>
<div class="abs fbtn" style="color:#fff">Submit</div>

<span class="dot" style="top:1027px"></span>
<div class="abs details" style="left:452px;top:1023px;color:#fff"><b>Portales 720</b><br>123 enim ad minim veniaml,<br>&nbsp;quis nostrud exerci</div>
<span class="dot" style="top:1076px"></span>
<div class="abs details" style="left:452px;top:1072px;color:#fff"><b>123 555 0190</b></div>
<span class="dot" style="top:1097px"></span>
<div class="abs details" style="left:452px;top:1093px;color:#fff;line-height:17px"><b>Mon - Thu : 9:00 - 14:00 / 16:00 - 19:00</b><br>&nbsp;<b>Fri : 9:00 - 14:00</b></div>
<span class="dot" style="top:1133px"></span>
<div class="abs details" style="left:452px;top:1129px;color:#fff">inqiry@portales720.example</div>

<svg class="abs" style="left:628px;top:954px" width="262" height="246" role="img" aria-label="Small road map of the office area with a location pin">
  <defs><linearGradient id="fm" x1="0" y1="0" x2="1" y2="1"><stop offset="0" stop-color="#f3efe3"/><stop offset="1" stop-color="#e8e2cf"/></linearGradient></defs>
  <polygon points="38,0 262,0 262,246 0,246" fill="url(#fm)"/>
</svg>

<div class="abs bottombar">
  <span class="abs" style="left:75px;top:8px">Copyright © 2017 Portales 720. All Rights Reserved.</span>
  <div class="abs social" style="left:556px;top:10px;color:#fff"><span></span><span></span><span></span></div>
</div>

</body>
</html>
```